Create a flyer that will catch your eye and make you want to call us for KELVOTH seamless Gutters

We are looking for a logo to help us with sales of our seamless gutter business, we are looking to expand, add loyal customers and increase our referral business.
We provide a turn key process from sales to install. we show up with our rolling factory, our truck spits out what seems to be an endless supply of gutter!
Each job is fabricated and installed to meet your homes design.

Target Market(s)

Treasure Coast of Florida, single story Homes

Font styles to use
Serif

Requirements
Must have
• Our Logo and Name on the flyer
Clean design with a clear message
call to action

```html
<!DOCTYPE html>
<html lang="en">
<head>
<meta charset="utf-8">
<title>Kelvoth Seamless Gutters Flyer</title>
<link href="https://fonts.googleapis.com/css2?family=Oswald:wght@300;400;600;700&family=Montserrat:wght@400;500&display=swap" rel="stylesheet">
<style>
  :root {
    --brand-green: #12a84a;
    --slate: #6b6b6d;
    --ink: #3a3a3c;
    --text-grey: #707072;
    --paper: #ffffff;
    --backdrop: #f2f2f2;
    --photo-top: #9aa28f;
    --photo-bottom: #c8cbca;
  }
  * { margin: 0; padding: 0; box-sizing: border-box; }
  html, body { width: 1200px; height: 764px; overflow: hidden; }
  body {
    background: var(--backdrop);
    display: flex; align-items: center; justify-content: center;
    font-family: "Montserrat", Arial, sans-serif;
  }
  .flyer {
    position: relative;
    width: 510px; height: 720px;
    background: var(--paper);
    box-shadow: 0 6px 18px rgba(0,0,0,0.18);
    overflow: hidden;
  }
  .info-column {
    position: absolute; left: 0; top: 0; width: 220px; height: 100%;
  }
  .accent-bar {
    position: absolute; left: 227px; top: 0; width: 10px; height: 100%;
    background: var(--brand-green);
  }
  .hero-photo {
    position: absolute; left: 247px; top: 0; width: 263px; height: 100%;
    background: linear-gradient(180deg, var(--photo-top) 0%, var(--photo-bottom) 100%);
  }
  .brand {
    position: absolute; left: 14px; top: 42px; width: 200px;
    display: flex; align-items: center; gap: 8px;
  }
  .brand-dot {
    width: 30px; height: 30px; border-radius: 50%;
    background: var(--brand-green); flex: none;
  }
  .brand-name {
    font-family: "Oswald", sans-serif; font-weight: 600;
    font-size: 40px; line-height: 1; color: var(--brand-green);
    letter-spacing: 0.5px;
  }
  .warranty {
    position: absolute; left: 0; top: 140px; width: 220px;
    text-align: center; font-family: "Oswald", sans-serif;
    color: var(--slate); text-transform: uppercase;
  }
  .warranty .lead { font-weight: 400; font-size: 17px; line-height: 1.25; }
  .warranty .headline { font-weight: 700; font-size: 38px; line-height: 1.12; color: #5f5f61; }
  .warranty .tail { font-weight: 400; font-size: 16.5px; line-height: 1.5; }
  .estimate-band {
    position: absolute; left: 0; top: 279px; width: 220px; height: 164px;
    background: var(--slate); color: var(--paper);
    text-align: center; font-family: "Oswald", sans-serif; text-transform: uppercase;
    padding-top: 14px;
  }
  .estimate-band .light { font-weight: 300; font-size: 24px; line-height: 1.1; }
  .estimate-band strong { font-weight: 700; }
  .estimate-band .bold { font-weight: 700; font-size: 22.5px; line-height: 1.18; }
  .estimate-band .rule {
    width: 76px; height: 1px; background: rgba(255,255,255,0.7); margin: 4px auto 6px;
  }
  .estimate-band .small {
    font-family: "Montserrat", sans-serif; font-size: 9px; letter-spacing: 0.3px; line-height: 1.2;
  }
  .about {
    position: absolute; left: 29px; top: 459px; width: 157px;
    font-size: 9.3px; line-height: 12.3px; color: var(--ink); text-align: justify;
  }
  .contact-title {
    position: absolute; left: 31px; top: 601px;
    font-family: "Oswald", sans-serif; font-weight: 700; font-size: 24px;
    line-height: 1; color: var(--brand-green); text-transform: uppercase;
  }
  .contact-list {
    position: absolute; left: 33px; top: 640px; list-style: none;
    font-size: 10.5px; line-height: 11.3px; color: var(--text-grey);
  }
  .contact-list li { display: flex; align-items: center; gap: 4px; }
  .contact-list svg { width: 8px; height: 8px; flex: none; }
  .address {
    position: absolute; left: 33px; top: 682px;
    font-size: 10.5px; line-height: 13.5px; color: #8a8a8c;
  }
</style>
</head>
<body>
  <main class="flyer">
    <section class="info-column">
      <div class="brand">
        <span class="brand-dot"></span>
        <span class="brand-name">Kelvoth</span>
      </div>

      <div class="warranty">
        <p class="lead">We provide the very best</p>
        <p class="headline">Warranty</p>
        <p class="tail">In the business and use the<br>best materials available.</p>
      </div>

      <div class="estimate-band">
        <p class="light">We provide <strong>free</strong> in</p>
        <p class="bold">Home estimates</p>
        <div class="rule"></div>
        <p class="small">AND ARE ADHERING TO</p>
        <p class="bold">Stringent Covid-19<br>protocals</p>
      </div>

      <p class="about">Kelvoth provides top quality seamless gutter system that will protect your home for many years. Our traveling gutter factory on wheels allows us to custom fit gutters to your homes specific needs at a competitive price. We take pride in our excellent customer service, professional installs and quality products.</p>

      <h2 class="contact-title">Contact us</h2>
      <ul class="contact-list">
        <li><svg viewBox="0 0 10 10"><circle cx="5" cy="5" r="4.3" fill="none" stroke="#12a84a" stroke-width="1.2"/><path d="M3.4 2.8l1 1-0.5 0.6a3 3 0 0 0 1.7 1.7l0.6-0.5 1 1-0.7 0.8C4.8 7.1 2.9 5.2 2.6 3.5z" fill="#12a84a"/></svg>+1 772 555 0148</li>
        <li><svg viewBox="0 0 10 10"><circle cx="5" cy="5" r="5" fill="#12a84a"/><rect x="2.6" y="3.4" width="4.8" height="3.2" fill="#fff"/><path d="M2.6 3.4L5 5.2 7.4 3.4" fill="none" stroke="#12a84a" stroke-width="0.6"/></svg>info@kelvoth.com</li>
        <li><svg viewBox="0 0 10 10"><circle cx="5" cy="5" r="5" fill="#12a84a"/><circle cx="5" cy="5" r="3" fill="none" stroke="#fff" stroke-width="0.6"/><path d="M2 5h6M5 2v6" stroke="#fff" stroke-width="0.6"/></svg>www.kelvoth.com</li>
      </ul>
      <p class="address">Your address, Suit # 000,<br>Dummy Street, City, State,</p>
    </section>

    <div class="accent-bar"></div>
    <div class="hero-photo" role="img" aria-label="Photo looking along a perforated white gutter guard on a mossy roof edge above a green lawn"></div>
  </main>
</body>
</html>
```